Business Card Design Project

Business Card design for Company in Web Services.
Would like it to have a grunge effect, maybe paint splashes.
Want something very unique and modern:

https://www.quarnelo.example/find?q=unique+business+card&hl=en&client=velbrook-a&tbo=u&rls=org.tandrel:en-US:official&tbm=isch&source=univ&sa=X&ei=Kp7rTWmhB4yz2RH48JKaQx&ved=0DFGRtBQ&biw=1320&bih=712
Updates

Ok I have increased the budget as I would like to change the logo a bit, I would like more of typography sketch or grunge logo, very modern, maybe a paint brush as the L, maybe dripping paint, am open to ideas.

Hi,

I have someone uploaded the concept of a logo, i would prefer. as i mentioned before I am open to any suggestions. Modern, but preferably artsy feeling.
Look forward to your design submissions

Industry/Entity Type

Paint

Requirements
Nice to have
• Would like some unique print features, perhaps, embossed, transparency, unique cut out. somethings along those lines.
Something that really shows design.

```html
<!DOCTYPE html>
<html lang="en">
<head>
<meta charset="utf-8">
<title>Business Card – dela Paz, Marco</title>
<link rel="stylesheet" href="https://fonts.googleapis.com/css2?family=Questrial&display=swap">
<style>
  :root {
    --page-bg: #ffffff;
    --card-black: #0b0b0b;
    --card-charcoal: #2a2a2a;
    --ray-pink: #e0157a;
    --ray-blue: #1e9fe0;
    --ray-green: #8cc63f;
    --ray-dark: #2b2f33;
    --text-light: #ffffff;
    --hole: #ffffff;
  }
  html, body {
    margin: 0;
    padding: 0;
    width: 732px;
    height: 1200px;
    overflow: hidden;
    background: var(--page-bg);
  }
  .canvas {
    position: relative;
    width: 732px;
    height: 1200px;
  }
  .card {
    position: absolute;
    left: 53px;
    top: 42px;
    width: 630px;
    height: 1095px;
  }
  .card-art {
    position: absolute;
    inset: 0;
    display: block;
  }
  .contact {
    position: absolute;
    left: 111px;
    top: 912px;
    color: var(--text-light);
    font-family: "Questrial", "Century Gothic", sans-serif;
  }
  .contact-name {
    margin: 0 0 6px;
    font-size: 50px;
    font-weight: 400;
    line-height: 1.1;
    letter-spacing: 0.5px;
  }
  .contact-line {
    margin: 0;
    font-size: 25px;
    font-style: italic;
    line-height: 1.25;
  }
</style>
</head>
<body>
<main class="canvas">
  <article class="card">
    <svg class="card-art" viewBox="0 0 630 1095" xmlns="http://www.w3.org/2000/svg">
      <defs>
        <linearGradient id="base-black" x1="0" y1="0" x2="1" y2="0">
          <stop offset="0" stop-color="var(--card-black)"/>
          <stop offset="0.5" stop-color="var(--card-charcoal)"/>
          <stop offset="1" stop-color="var(--card-black)"/>
        </linearGradient>
        <radialGradient id="glow-pink" cx="0.15" cy="0.62" r="0.45">
          <stop offset="0" stop-color="var(--ray-pink)" stop-opacity="0.95"/>
          <stop offset="1" stop-color="var(--ray-pink)" stop-opacity="0"/>
        </radialGradient>
        <radialGradient id="glow-blue" cx="0.3" cy="0.3" r="0.55">
          <stop offset="0" stop-color="var(--ray-blue)" stop-opacity="0.9"/>
          <stop offset="1" stop-color="var(--ray-blue)" stop-opacity="0"/>
        </radialGradient>
        <radialGradient id="glow-green" cx="0.7" cy="0.75" r="0.5">
          <stop offset="0" stop-color="var(--ray-green)" stop-opacity="0.9"/>
          <stop offset="1" stop-color="var(--ray-green)" stop-opacity="0"/>
        </radialGradient>
        <radialGradient id="glow-top" cx="0.9" cy="0.05" r="0.35">
          <stop offset="0" stop-color="var(--ray-pink)" stop-opacity="0.8"/>
          <stop offset="1" stop-color="var(--ray-pink)" stop-opacity="0"/>
        </radialGradient>
      </defs>

      <rect class="card-base" width="630" height="1095" fill="url(#base-black)"/>

      <g class="light-rays" role="img" aria-label="Abstract overlapping light rays in pink, blue and green over a dark textured ground">
        <path d="M0 0 H630 V813 C580 845 500 872 400 876 C280 880 110 820 0 668 Z" fill="var(--ray-dark)"/>
        <path d="M0 0 H630 V813 C580 845 500 872 400 876 C280 880 110 820 0 668 Z" fill="url(#glow-blue)"/>
        <path d="M0 0 H630 V813 C580 845 500 872 400 876 C280 880 110 820 0 668 Z" fill="url(#glow-green)"/>
        <path d="M0 0 H630 V813 C580 845 500 872 400 876 C280 880 110 820 0 668 Z" fill="url(#glow-pink)"/>
        <path d="M0 0 H630 V813 C580 845 500 872 400 876 C280 880 110 820 0 668 Z" fill="url(#glow-top)"/>
      </g>

      <path class="cut-line" d="M0 668 C110 820 280 880 400 876 C500 872 580 845 630 813"
            fill="none" stroke="var(--text-light)" stroke-width="2" stroke-dasharray="7 5"/>

      <circle class="punch-hole" cx="536" cy="98" r="30" fill="var(--hole)"/>
      <circle class="punch-hole" cx="63" cy="814" r="31" fill="var(--hole)"/>
    </svg>

    <div class="contact">
      <h1 class="contact-name">dela Paz, Marco</h1>
      <p class="contact-line">+63 0900.555.0142</p>
      <p class="contact-line">email: kaito7serv@mailbox.example</p>
    </div>
  </article>
</main>
</body>
</html>
```